Web Design Project (Mente Lumo)

We are going to do a therapy template to a psychologist. The site already exists, adress: www.mentelumo.net. So, its a total redesign job. I'm from Brazil, the language is PT-BR, so I'm gonna translate what you think be necessary. You can use the current structure from the website as a base to the new design. Check this template to see what I usually like: http://www.layoutkestrel.com/demo/51907.html
Updates

I'm waiting for new creative designs. The 'structure' image is just for 'pb'.

Requirements
Must have
• We need a modern menu, it should use a cool font style and make some kind of effect and little noise when the user pass over with the mouse (FLASH/HTML 5). The main page must emphasize the fact that we offer online treatment, like a picture or frame saying "Online Treatment, click here". It must also show the therapist picture and her name. The colors need to pass a tranquility feeling. The clinic telephone must always be present, doesn't matter which page the user is. The website must adapt to any resolution above 1024x768, crossbrowsing and accept javascript (I'll use www.slotvira.com, so its necessary embed code)
Nice to have
• I would appreciate if there was some kind of slow background animation, passing behind the text using the transparency.
Should not have
• Can't take too long to load, and won't have news or blog

```html
<!DOCTYPE html>
<html lang="en">
<head>
<meta charset="utf-8">
<title>Mente Lumo</title>
<link rel="stylesheet" href="https://fonts.googleapis.com/css2?family=Open+Sans:wght@400;600;700&family=Muli:wght@400;600&family=Arvo&family=Lora:ital@1&display=swap">
<style>
:root{
  --cyan-top:#62dcef;
  --cyan:#1ab3d0;
  --cyan-deep:#0e9ab8;
  --teal-text:#1590a8;
  --navy:#1d4d84;
  --navy-deep:#0b2a5c;
  --paper:#f3f1eb;
  --body:#7a7a7a;
  --ink:#333;
  --green:#3aa63a;
  --green-dark:#1f7d22;
  --red:#c8171b;
}
*{margin:0;padding:0;box-sizing:border-box}
html,body{width:941px;height:1200px;overflow:hidden}
body{position:relative;background:var(--paper);font-family:"Muli",sans-serif;color:var(--body)}
.abs{position:absolute}
.header{left:0;top:0;width:941px;height:132px;background:linear-gradient(var(--cyan-top),var(--cyan) 80%,var(--cyan-deep))}
.header-wave{left:0;top:116px;width:941px;height:20px}
.brand{left:110px;top:44px;display:flex;align-items:center;gap:8px;color:#fff;font-family:"Open Sans",sans-serif;font-weight:700;font-size:20px}
.brand i{display:block;width:30px;height:30px;border:3px solid #fff;border-radius:50%}
.lang{left:753px;top:5px;font:11px "Open Sans",sans-serif;color:#fff}
.top-phone{left:696px;top:27px;font:700 19px "Open Sans",sans-serif;color:#fff}
.top-mail{left:731px;top:51px;font:11px "Open Sans",sans-serif;color:#e8fbff}
.nav{left:317px;top:84px;display:flex;gap:0;font:700 13px "Open Sans",sans-serif;color:#fff}
.nav span{padding:4px 11px;border-radius:5px}
.nav .active{background:#fff;color:#333}
.slider{left:0;top:128px;width:941px;height:315px;background:linear-gradient(90deg,#bfc4c8,#e6e8ea 40%,#d7dadd 70%,#aeb3b7)}
.slide-photo{left:110px;top:138px;width:340px;height:305px;background:linear-gradient(#d9b58e,#f1ede8 55%,#e4e8ec)}
.slide-band{left:410px;top:212px;width:232px;height:160px}
.slide-caption{left:468px;top:244px;font:24px/26px "Arvo",serif;color:#fff}
.slide-panel{left:643px;top:196px;width:187px;height:247px;background:var(--navy-deep)}
.slide-panel .top{height:122px;background:var(--cyan);padding:10px 15px;color:#fff}
.slide-panel h3{font:20px/21px "Arvo",serif;font-weight:400}
.slide-panel p{font:600 10px/13px "Open Sans",sans-serif;margin-top:4px}
.slide-panel .art{height:125px;background:radial-gradient(circle at 50% 45%,#e05a2a 0,#3b5fc0 30%,var(--navy-deep) 70%)}
.slider-foot{left:0;top:420px;width:941px;height:30px}
.dots{left:437px;top:458px;display:flex;gap:3px}
.dots i{width:11px;height:11px;border-radius:50%;background:#ddd;border:1px solid #bbb}
.dots i:first-child{background:var(--teal-text);border-color:var(--teal-text)}
.card{left:112px;top:512px;width:238px;height:545px;background:#fff;border:1px solid #e2e2e2;border-radius:6px;box-shadow:0 1px 4px rgba(0,0,0,.08)}
.card-head{height:41px;background:linear-gradient(#eafbfe,#bdeef7);border-radius:6px 6px 0 0;padding:8px 14px;font:600 20px "Muli",sans-serif;color:var(--teal-text)}
.text{font-size:11.3px;line-height:16.2px}
.who-intro{left:127px;top:566px;width:210px}
.portrait{left:127px;top:627px;width:110px;height:110px;background:linear-gradient(#6b6b6b,#bdbdbd)}
.name{left:249px;top:670px;font:17px/17px "Muli",sans-serif;color:var(--teal-text)}
.role{left:251px;top:713px;font:10px "Open Sans",sans-serif;color:#444}
.role small{display:block;font-size:8px;color:#777}
.who-body{left:127px;top:756px;width:212px}
.more{font-size:11px;color:var(--teal-text)}
.about-title{left:380px;top:521px;font:600 20px "Muli",sans-serif;color:var(--ink)}
.about-body{left:380px;top:566px;width:232px}
.call-tag{left:703px;top:516px;background:var(--red);color:#fff;font:700 13px "Open Sans",sans-serif;padding:2px 7px;border-radius:4px}
.call-icon{left:648px;top:533px}
.call-nums{left:703px;top:541px;font:italic 19px/22px "Lora",serif;color:var(--green)}
.online{left:643px;top:606px;width:186px;height:197px;border-radius:4px;background:linear-gradient(var(--green),var(--green-dark));text-align:center;color:#fff}
.online h4{font:600 17px "Muli",sans-serif;color:#f1f79b;margin-top:8px}
.online p{font:16px "Muli",sans-serif}
.online strong{display:block;font:600 17px "Muli",sans-serif;margin-top:4px}
.online .art{width:90px;height:70px;margin:8px auto 0;background:linear-gradient(#d8e6d8,#7fa37f);border-radius:4px}
.click{left:670px;top:788px;width:132px;height:28px;border-radius:14px;background:linear-gradient(#fff,#d8d8d8);box-shadow:0 1px 3px rgba(0,0,0,.35);font:700 13px "Open Sans",sans-serif;color:#333;display:flex;align-items:center;justify-content:center;gap:10px}
.click i{width:18px;height:18px;border-radius:50%;background:var(--green-dark)}
.loc-title{left:645px;top:833px;font:600 15px "Muli",sans-serif;color:var(--ink)}
.loc-box{left:643px;top:857px;width:186px;height:197px;background:#fff;border:1px solid #e2e2e2}
.map{left:651px;top:865px;width:170px;height:122px;background:linear-gradient(135deg,#ecebe6,#dfe5d6)}
.loc-addr{left:651px;top:997px;width:170px;text-align:center;font:11px/14px "Open Sans",sans-serif;color:#222}
.footer{left:0;top:1093px;width:941px;height:107px;background:linear-gradient(var(--cyan),var(--cyan-top))}
.footer-wave{left:0;top:1086px;width:941px;height:16px}
.social{left:430px;top:1108px;display:flex;gap:5px}
.social i{width:23px;height:23px;border-radius:3px;background:#0b4a60}
.foot-links{left:0;top:1140px;width:941px;text-align:center;font:11px "Open Sans",sans-serif;color:#0d2a33}
.foot-line{left:195px;top:1163px;width:551px;height:1px;background:rgba(255,255,255,.5)}
.copy{left:0;top:1172px;width:941px;text-align:center;font:11px "Open Sans",sans-serif;color:#0d2a33}
</style>
</head>
<body>
<div class="abs header"></div>
<svg class="abs header-wave" viewBox="0 0 941 20" preserveAspectRatio="none"><path d="M0 4 Q470 16 941 4 L941 20 L0 20Z" fill="#fff"/></svg>
<div class="abs brand"><i></i>Mente Lumo</div>
<div class="abs lang">Select Language ▾</div>
<div class="abs top-phone">+(11) 4820-1936</div>
<div class="abs top-mail">ines.valmor@mail.net</div>
<nav class="abs nav"><span class="active">HOME</span><span>TREATMENTS</span><span>QUESTIONS</span><span>ASK THE EXPERT</span><span>LOCATION</span><span>CONTACT</span></nav>

<div class="abs slider" role="img" aria-label="Blurred clinic corridor background"></div>
<div class="abs slide-photo" role="img" aria-label="Smiling doctor holding a stethoscope"></div>
<svg class="abs slide-band" viewBox="0 0 232 160"><path d="M38 2 L232 12 L232 160 L10 150 L40 80Z" fill="#1d4d84" opacity=".95"/></svg>
<div class="abs slide-caption">The Cognitive<br>Therapy is as<br>a Method of<br>Interpreting...</div>
<div class="abs slide-panel">
  <div class="top"><h3>NEQUE<br>PORRO EST</h3><p>Lorem ipsum dolor sit amet, consectetur adipisicing elit, sed do eiusmod tempor incididunt ut labore et dolore magna aliqua.</p></div>
  <div class="art" role="img" aria-label="Glowing brain inside a head profile"></div>
</div>
<svg class="abs slider-foot" viewBox="0 0 941 30" preserveAspectRatio="none"><path d="M0 10 Q470 30 941 10 L941 30 L0 30Z" fill="#f3f1eb"/></svg>
<div class="abs dots"><i></i><i></i><i></i><i></i><i></i></div>

<section class="abs card"><div class="card-head">Who Am I?</div></section>
<p class="abs text who-intro">The Cognitive Therapy is as a method of interpreting mental contents and processes (cognitions),</p>
<div class="abs portrait" role="img" aria-label="Portrait of the therapist"></div>
<div class="abs name">Inês<br>Valmor</div>
<div class="abs role">Psicòlaga:<small>CRP: 6/204817</small></div>
<div class="abs text who-body">
  <p>Alden Brecht, creator of Cognitive Therapy, states that cognition, not emotion, is the essential factor in depression, which Brecht describes as thought disorder, and not emotional. He claims that the negativity was not a depressive symptom, but has a central role in the installation and maintenance of the disorder.</p><br>
  <p>The sessions and the therapeutic process are semi-structured, involving tasks between sessions, and is focused on the specific problems of patients and the therapeutic goals.</p><br>
  <p class="more">Read More ⊕</p>
</div>

<h2 class="abs about-title">About Us</h2>
<div class="abs text about-body">
  <p>Every mental disorder originates in thought. The Cognitive Therapy education through the search of his emotional balance. To do so, establish strategies is of real importance to the resolution of complaints. When the individual has a balanced operation, it can have a greater resistance facing the adversities that happen in the day-to-day. To understand the nature of a disease, we must understand the nature of the individual's relationships with the world that is around them.</p><br>
  <p>Alden Brecht, creator of Cognitive Therapy, states that cognition, not emotion, is the essential factor in depression, which Brecht describes as thought disorder, and not emotional. He claims that the negativity was not a depressive symptom, but has a central role in the installation and maintenance of the disorder.</p><br>
  <p>The sessions and the therapeutic process are semi-structured, involving tasks between sessions, and is focused on the specific problems of patients and the therapeutic goals.</p><br>
  <p class="more">Read More ⊕</p>
</div>

<div class="abs call-tag">Call Now!</div>
<svg class="abs call-icon" width="48" height="52" viewBox="0 0 48 52"><path d="M4 14 Q24 2 44 14 L40 22 L32 18 L32 14 Q24 11 16 14 L16 18 L8 22Z" fill="#c8171b"/><path d="M10 24 L38 24 L44 46 L4 46Z" fill="#c8171b"/><circle cx="24" cy="35" r="7" fill="#fff"/><circle cx="24" cy="35" r="3" fill="#c8171b"/></svg>
<div class="abs call-nums">(11) 9514-3307<br>(11) 7362-0184</div>
<div class="abs online">
  <h4>Online Treatment</h4>
  <p>Likely suffer some</p>
  <strong>Disturbance</strong>
  <div class="art" role="img" aria-label="Person stepping out of a laptop screen"></div>
</div>
<div class="abs click">CLICK HERE <i></i></div>

<h3 class="abs loc-title">Our Location</h3>
<div class="abs loc-box"></div>
<div class="abs map" role="img" aria-label="Street map of the clinic area"></div>
<p class="abs loc-addr">Lindel Hill Street, 412, 5th floor, room 52 - Center - Vila Serena, SP</p>

<div class="abs footer"></div>
<svg class="abs footer-wave" viewBox="0 0 941 16" preserveAspectRatio="none"><path d="M0 16 L0 10 Q470 0 941 10 L941 16Z" fill="#1ab3d0"/></svg>
<div class="abs social"><i></i><i></i><i></i></div>
<div class="abs foot-links">Home &nbsp;|&nbsp; Treatments &nbsp;|&nbsp; Questions &nbsp;|&nbsp; Ask the expert &nbsp;|&nbsp; Location &nbsp;|&nbsp; Contact</div>
<div class="abs foot-line"></div>
<div class="abs copy">Copyright © 2012 - Todos os direitos reservados</div>
</body>
</html>
```